Website Design for A Nook for Grandpas

Please design and code a new website.
Here are the sites I like best:
http://www.sailbeacon.net/alternate/
http://www.wheelsgiving.net
Please make it similar but look at the competitor site (below) for images and wording. This is NOT a car donation site. It's a senior lead placement site like https://www.eldernestfinder.net. I just like this sites above as a lead generation sites.
Competitor site:
https://www.eldernestfinder.net (use ideas / verbiage from this site)
Updates
Competitor site:

```html
<!DOCTYPE html>
<html lang="en">
<head>
<meta charset="utf-8">
<title>A Nook for Grandpas — Senior Living Advisors</title>
<link href="https://fonts.googleapis.com/css2?family=Arvo:ital,wght@0,400;0,700;1,400;1,700&family=Lato:ital,wght@0,400;0,700;1,400&family=Oswald:wght@400;500&display=swap" rel="stylesheet">
<style>
:root{
  --navy:#112b4d;
  --navy-deep:#0c2240;
  --green:#8dc63f;
  --blue:#1b4f93;
  --text:#333;
  --muted:#666;
  --line:#d9dde3;
  --star:#f26522;
}
*{box-sizing:border-box;margin:0;padding:0}
html,body{width:1200px;height:3316px;overflow:hidden;background:#fff}
body{position:relative;font-family:'Lato',sans-serif;color:var(--text)}
.abs{position:absolute}
.serif{font-family:'Arvo',serif}
.accent{color:var(--green);font-style:italic;font-weight:700}

/* header */
.brand{left:142px;top:24px;display:flex;align-items:center;gap:12px}
.brand-dot{width:34px;height:34px;border-radius:50%;background:var(--green)}
.brand-name{font-family:'Arvo',serif;font-size:30px;color:var(--navy)}
.call{left:648px;top:22px;display:flex;align-items:center;gap:10px}
.call small{display:block;font-size:10px;color:var(--muted)}
.call strong{font-family:'Oswald',sans-serif;font-weight:400;font-size:24px;color:var(--navy)}
.badge{left:865px;top:20px;width:110px;height:47px;background:var(--navy);border-radius:4px}
.lang{left:1025px;top:36px;width:16px;height:16px;border-radius:50%;background:#c9d3e6}

/* nav */
.nav{left:0;width:1200px;background:var(--navy);display:flex;justify-content:flex-start}
.nav ul{list-style:none;display:flex;margin-left:142px}
.nav li{font-family:'Oswald',sans-serif;color:#fff;font-size:15.5px;padding:0 17px;text-transform:uppercase;display:flex;align-items:center}
.nav li.active{background:var(--green)}
.top-nav{top:92px;height:49px}
.foot-nav{top:3202px;height:76px}
.foot-nav ul{margin-left:150px}

/* hero */
.hero{left:0;top:141px;width:1200px;height:540px;background:linear-gradient(100deg,#8c9aa4 0%,#c8cfd3 30%,#e6dccb 55%,#b7c7d2 75%,#e9e2d4 100%)}
.hero-shade{left:0;top:520px;width:1200px;height:161px;background:linear-gradient(to bottom,rgba(0,0,0,0),rgba(0,0,0,.45))}
.inquiry{left:694px;top:179px;width:364px;height:409px;background:#f4f5f6;padding:30px 29px}
.inquiry h3{font-family:'Arvo',serif;font-weight:400;font-size:24px;text-align:center;color:var(--navy);margin-bottom:20px}
.inquiry h3 span{color:var(--green)}
.field{display:flex;height:42px;border:1px solid var(--line);background:#fff;margin-bottom:12px;font-size:13px;color:var(--muted)}
.field i{width:40px;border-right:1px solid var(--line);display:flex;align-items:center;justify-content:center}
.field i b{width:10px;height:10px;background:#555;border-radius:2px}
.field span{padding:12px 17px}
.field.tall{height:69px}
.btn{background:var(--green);color:#fff;font-family:'Arvo',serif;font-weight:700;font-size:15px;text-align:center}
.inquiry .btn{height:38px;line-height:38px;margin-top:8px}
.tagline{left:0;width:1200px;top:610px;text-align:center;font-family:'Arvo',serif;color:#fff;font-size:31px;text-shadow:0 1px 3px rgba(0,0,0,.4)}

/* support */
.support-photo{left:142px;top:773px;width:422px;height:387px;background:linear-gradient(160deg,#7fb0df,#c6d6e1 55,#8a8f8e)}
.support{left:615px;top:770px;width:450px}
.support h2{font-family:'Arvo',serif;font-weight:400;font-size:28px;color:var(--navy);line-height:42px}
.support h2 .accent{font-size:31px}
.support p{font-size:14px;line-height:24px;margin:10px 0 14px;color:#444}
.features{list-style:none}
.features li{display:flex;align-items:center;gap:13px;height:48px;font-size:14px}
.features svg{flex:none}

/* no cost */
.nocost{left:142px;top:1232px;width:916px;height:174px;border:1px solid #eef0f2;box-shadow:0 8px 18px rgba(141,198,63,.18);text-align:center;padding-top:36px}
.nocost h2{font-family:'Arvo',serif;font-style:italic;font-weight:700;font-size:31px;color:var(--navy)}
.nocost p{font-style:italic;font-size:17px;margin:6px 0 6px;color:#333}
.nocost .phone{font-family:'Oswald',sans-serif;font-weight:500;font-size:32px;color:var(--blue)}
.nocost .phone span{color:var(--green)}

/* advisor */
.advisor-bg{left:0;top:1510px;width:1200px;height:494px;background:linear-gradient(90deg,#1d2d45 0%,#2d3c52 25%,#1f3150 45%,#1d3458 100%)}
.advisor-box{left:424px;top:1567px;width:634px;height:388px;background:#fff;padding:40px 42px;text-align:center}
.advisor-box h2{font-family:'Arvo',serif;font-style:italic;font-weight:400;font-size:29px;color:var(--navy)}
.advisor-box p{font-size:14px;margin:14px 0 30px}
.perks{display:flex;justify-content:space-between}
.perk{width:170px;font-size:14px;line-height:18px;color:#333}
.perk svg{display:block;margin:0 auto 12px}
.finder{display:flex;margin-top:30px;border:1px solid var(--line);height:48px}
.finder span{flex:1;text-align:left;padding:15px 18px;font-size:13px;color:#444}
.finder .btn{width:248px;line-height:44px;margin:1px}

/* testimonials */
.reviews-title{left:0;width:1200px;top:2076px;text-align:center;font-family:'Arvo',serif;font-size:29px;color:var(--navy)}
.review{top:2167px;width:437px;height:204px;border:1px solid #e3e6ea;padding:32px 22px}
.review .who{display:flex;gap:14px;align-items:center}
.avatar{width:56px;height:56px;border-radius:50%;background:#d8dee5;border:2px solid var(--green)}
.who h4{font-family:'Arvo',serif;font-size:14px;color:var(--navy)}
.stars{color:var(--star);font-size:11px;letter-spacing:2px}
.quote{position:absolute;right:20px;top:30px}
.review p{font-size:12.5px;line-height:23px;margin-top:16px;color:#333}
.arrow{top:2252px}

/* veterans */
.vets{left:0;top:2450px;width:1200px;height:317px;background:linear-gradient(90deg,#1c3763 0%,#233f6e 45%,#3a3d61 60%,#2e3a5f 100%);text-align:center;color:#fff;padding-top:72px}
.vets h2{font-family:'Arvo',serif;font-style:italic;font-weight:700;font-size:33px}
.vets h2 span{color:var(--green)}
.vets p{font-size:16px;line-height:28px;width:900px;margin:12px auto 18px}
.vets .btn{display:inline-block;width:130px;height:38px;line-height:38px;font-size:14px}

/* states */
.states-title{left:0;width:1200px;top:2864px;text-align:center;font-family:'Arvo',serif;font-size:29px;color:var(--navy)}
.states{top:2928px;list-style:none;font-size:12.5px;color:#333}
.states li{height:25.5px;padding-left:14px;position:relative}
.states li::before{content:"›";position:absolute;left:0;top:-2px;color:var(--green);font-size:15px}

/* footer */
.copyright{left:0;top:3278px;width:1200px;height:38px;background:var(--green);display:flex;align-items:center;justify-content:space-between;padding:0 142px 0 143px;font-size:12px;color:#1a2a3a}
.social{display:flex;gap:6px}
.social span{width:25px;height:25px;border-radius:50%;background:var(--navy)}
</style>
</head>
<body>

<header>
  <div class="abs brand"><span class="brand-dot"></span><span class="brand-name">A Nook for Grandpas</span></div>
  <div class="abs call">
    <svg width="30" height="30" viewBox="0 0 24 24" fill="none" stroke="#1b4f93" stroke-width="1.6"><path d="M5 3h4l2 5-2.5 1.5a11 11 0 0 0 6 6L16 13l5 2v4a2 2 0 0 1-2 2A16 16 0 0 1 3 5a2 2 0 0 1 2-2z"/></svg>
    <div><small>Talk to a local advisor for FREE</small><strong>(123) 555-0172</strong></div>
  </div>
  <div class="abs badge" role="img" aria-label="Accreditation badge"></div>
  <div class="abs lang" role="img" aria-label="Language selector"></div>
</header>

<nav class="abs nav top-nav">
  <ul><li class="active">Assisted Living</li><li>Memory Care</li><li>Nursing Homes</li><li>More Living Options ▾</li><li>Planning &amp; Advice</li><li>How Our Service Works</li></ul>
</nav>

<section>
  <div class="abs hero" role="img" aria-label="Smiling senior couple on a sunny beach"></div>
  <div class="abs hero-shade"></div>
  <form class="abs inquiry">
    <h3>Quick <span>Inquiry</span></h3>
    <div class="field"><i><b></b></i><span>Name</span></div>
    <div class="field"><i><b></b></i><span>Phone</span></div>
    <div class="field"><i><b></b></i><span>Email</span></div>
    <div class="field tall"><i><b></b></i><span>Message</span></div>
    <div class="btn">Submit Now</div>
  </form>
  <p class="abs tagline">You know your family.We know <em>Senior Living.</em></p>
</section>

<section>
  <div class="abs support-photo" role="img" aria-label="Group of cheerful seniors with bicycles at the beach"></div>
  <div class="abs support">
    <h2>The support you need to make the<br><span class="accent">Right Choice</span></h2>
    <p>Lorem ipsum dolor sit amet, consectetuer adipiscing elit, sed nonummy nibh euismod tincidunt ut laoreet dolore magna aliquam erat</p>
    <ul class="features">
      <li><svg width="36" height="36" viewBox="0 0 36 36"><circle cx="18" cy="18" r="18" fill="#1b4f93"/><circle cx="18" cy="13" r="4" fill="none" stroke="#fff" stroke-width="1.5"/><path d="M11 26c0-4 3-7 7-7s7 3 7 7z" fill="none" stroke="#fff" stroke-width="1.5"/></svg>Dedicated local advisor</li>
      <li><svg width="36" height="36" viewBox="0 0 36 36"><circle cx="18" cy="18" r="18" fill="#1b4f93"/><path d="M10 18l8-7 8 7M12 17v9h12v-9" fill="none" stroke="#fff" stroke-width="1.5"/></svg>Hand-picked list of communities to match your needs</li>
      <li><svg width="36" height="36" viewBox="0 0 36 36"><circle cx="18" cy="18" r="18" fill="#8dc63f"/><path d="M21 13h-4a2 2 0 0 0 0 5h2a2 2 0 0 1 0 5h-4M18 10v16" fill="none" stroke="#fff" stroke-width="1.5"/></svg>Full details &amp; pricing</li>
      <li><svg width="36" height="36" viewBox="0 0 36 36"><circle cx="18" cy="18" r="18" fill="#1b4f93"/><rect x="11" y="12" width="14" height="13" fill="none" stroke="#fff" stroke-width="1.5"/><path d="M11 16h14" stroke="#fff" stroke-width="1.5"/></svg>Help scheduling tours</li>
      <li><svg width="36" height="36" viewBox="0 0 36 36"><circle cx="18" cy="18" r="18" fill="#1b4f93"/><path d="M9 13h12v10H9zM21 16h4l3 3v4h-7" fill="none" stroke="#fff" stroke-width="1.5"/><circle cx="13" cy="24" r="1.8" fill="#fff"/><circle cx="24" cy="24" r="1.8" fill="#fff"/></svg>Move in support</li>
    </ul>
  </div>
</section>

<section class="abs nocost">
  <h2>There's No Cost To You</h2>
  <p>We work with over 20,000 senior living communities. Our community partners pay us for placement services.</p>
  <div class="phone">CALL <span>866-555-0148</span></div>
</section>

<section>
  <div class="abs advisor-bg" role="img" aria-label="Smiling local advisor in a suit, in an office"></div>
  <div class="abs advisor-box">
    <h2>Your <span class="accent">Local Advisor</span> Informs. You Decide.</h2>
    <p>Over 400 senior advisors across the U.S. and Canada are ready to help your family with:</p>
    <div class="perks">
      <div class="perk"><svg width="34" height="44" viewBox="0 0 34 44" fill="none" stroke="#8dc63f" stroke-width="1.8"><path d="M17 42S3 26 3 16a14 14 0 0 1 28 0c0 10-14 26-14 26z"/><circle cx="17" cy="16" r="5"/></svg>Insider's tips for the area near you</div>
      <div class="perk"><svg width="46" height="42" viewBox="0 0 46 42" fill="none" stroke="#8dc63f" stroke-width="1.8"><path d="M23 40S2 26 2 13A11 11 0 0 1 23 8a11 11 0 0 1 21 5c0 13-21 27-21 27z"/></svg>Advice tailored to your unique situation</div>
      <div class="perk"><svg width="42" height="36" viewBox="0 0 42 36" fill="none" stroke="#8dc63f" stroke-width="1.8"><circle cx="4" cy="4" r="3"/><circle cx="4" cy="18" r="3"/><circle cx="4" cy="32" r="3"/><path d="M13 4h28M13 18h28M13 32h28"/></svg>Time saving know-how and resources</div>
    </div>
    <div class="finder"><span>Enter city or postal code</span><div class="btn">Find An Advisor Near You</div></div>
  </div>
</section>

<section>
  <h2 class="abs reviews-title">93% Of Our <span class="accent">Customers Recommend</span> Our Service</h2>
  <svg class="abs arrow" style="left:88px" width="22" height="42" viewBox="0 0 22 42" fill="none" stroke="#1b4f93" stroke-width="1.5"><path d="M20 1L2 21l18 20"/></svg>
  <svg class="abs arrow" style="left:1090px" width="22" height="42" viewBox="0 0 22 42" fill="none" stroke="#8dc63f" stroke-width="1.5"><path d="M2 1l18 20L2 41"/></svg>
  <article class="abs review" style="left:142px">
    <div class="who"><div class="avatar" role="img" aria-label="Reviewer portrait"></div><div><h4>Marla Quint</h4><div class="stars">★★★★★</div></div></div>
    <svg class="quote" width="50" height="42" viewBox="0 0 50 42" fill="#e4f1d3"><path d="M0 12h20v30H0zM28 12h20v30H28zM0 12q4-12 16-12v6Q8 8 8 12zM28 12q4-12 16-12v6q-8 2-8 6z"/></svg>
    <p>Lorem ipsum dolor sit amet, consectetuer adipiscing elit, sed diam nonummy nibh euismod tincidunt ut laoreet dolore magna aliquam erat volutpat. Ut wisi enim ad minim veniam, quis</p>
  </article>
  <article class="abs review" style="left:622px">
    <div class="who"><div class="avatar" role="img" aria-label="Reviewer portrait"></div><div><h4>Dorian Pell</h4><div class="stars">★★★★★</div></div></div>
    <svg class="quote" width="50" height="42" viewBox="0 0 50 42" fill="#e4f1d3"><path d="M0 12h20v30H0zM28 12h20v30H28zM0 12q4-12 16-12v6Q8 8 8 12zM28 12q4-12 16-12v6q-8 2-8 6z"/></svg>
    <p>Lorem ipsum dolor sit amet, consectetuer adipiscing elit, sed diam nonummy nibh euismod tincidunt ut laoreet dolore magna aliquam erat volutpat. Ut wisi enim ad minim veniam, quis</p>
  </article>
</section>

<section class="abs vets" role="region" aria-label="Veteran's aid, over a waving flag backdrop">
  <h2>Access Up To <span>$2,000 Per Month</span> In Veteran's Aid</h2>
  <p>We work with Veterans every day. Most veteran families do not know of a key benefit available to them &amp; their families. It's called the Veteran's Aid &amp; Attendance benefit. This benefit can help pay for senior living &amp; home care.</p>
  <div class="btn">Learn More</div>
</section>

<section>
  <h2 class="abs states-title">Senior Assisted <span class="accent">Living by State</span></h2>
  <ul class="abs states" style="left:142px"><li>Alabama</li><li>Arizona</li><li>Arkansas</li><li>California</li><li>Colorado</li><li>Connecticut</li><li>Delaware</li></ul>
  <ul class="abs states" style="left:287px"><li>District of Columbia</li><li>Florida</li><li>Georgia</li><li>Hawaii</li><li>Idaho</li><li>Illinois</li><li>Indiana</li></ul>
  <ul class="abs states" style="left:479px"><li>Iowa</li><li>Kansas</li><li>Kentucky</li><li>Louisiana</li><li>Maine</li><li>Maryland</li><li>Massachusetts</li></ul>
  <ul class="abs states" style="left:640px"><li>Michigan</li><li>Minnesota</li><li>Mississippi</li><li>Missouri</li><li>Montana</li><li>Nebraska</li><li>Nevada</li></ul>
  <ul class="abs states" style="left:780px"><li>New Hampshire</li><li>New Jersey</li><li>New Mexico</li><li>New York</li><li>North Carolina</li><li>North Dakota</li><li>Ohio</li></ul>
  <ul class="abs states" style="left:949px"><li>Oklahoma</li><li>Oregon</li><li>Pennsylvania</li><li>Rhode Island</li><li>South Carolina</li><li>South Dakota</li><li>Tennessee</li></ul>
</section>

<footer>
  <nav class="abs nav foot-nav">
    <ul><li>Assisted Living</li><li>Memory Care</li><li>Nursing Homes</li><li>More Living Options ▾</li><li>Planning &amp; Advice</li><li>How Our Service Works</li></ul>
  </nav>
  <div class="abs copyright">
    <span>Copyright 2019 A Nook for Grandpas. All Rights Reserved.</span>
    <div class="social"><span></span><span></span><span></span><span></span></div>
  </div>
</footer>

</body>
</html>
```